Dario Venti Pools , pool construction for residential properties and pool renovations

I have been involved in the pool industry for over 20years and looking to start my own buisnes. My brother and I are teaming up together to make this happen . We will be doing pool renovations to existing old pools "pool makeovers" and also owner builder pools which will save a lot of money in overall cost of a new pool construction. Cards need to be creative not a generic photo of pool ,let's be different.

Target Market(s)

Home owners

Industry/Entity Type

Pool Service

Contact Information for Business Card

Owner builder pools , Pool renovations

Font styles to use
Sans Serif

Colors

Designer to choose colors to be used in the design.

Requirements
Must have
• Mobile number , web , email
Nice to have
• Be creative

```html
<!DOCTYPE html>
<html lang="en">
<head>
<meta charset="utf-8">
<title>Dario Venti Pools – Business Card</title>
<link rel="stylesheet" href="https://fonts.googleapis.com/css2?family=Montserrat:wght@400;500;800&display=swap">
<style>
  :root {
    --navy: #1f1a4d;
    --sky: #1ba7e3;
    --ink: #3b3f4a;
    --water-light: #4cc3f0;
    --water-mid: #22a3e0;
    --water-deep: #1d3fa6;
    --water-dark: #0f2478;
    --paper: #ffffff;
  }
  html, body {
    margin: 0;
    padding: 0;
    overflow: hidden;
    background: var(--paper);
  }
  .card {
    position: relative;
    width: 1200px;
    height: 686px;
    overflow: hidden;
    background: var(--paper);
    font-family: "Montserrat", sans-serif;
  }
  .water {
    position: absolute;
    inset: 0;
    width: 1200px;
    height: 686px;
  }
  .brand-name {
    position: absolute;
    left: 84px;
    top: 78px;
    margin: 0;
    font-weight: 800;
    font-size: 128px;
    line-height: 1;
    letter-spacing: -4px;
    color: var(--navy);
    white-space: nowrap;
  }
  .brand-name .brand-sub {
    position: absolute;
    left: 284px;
    top: 166px;
    font-size: 50px;
    letter-spacing: 16px;
  }
  .contact {
    position: absolute;
    left: 88px;
    top: 372px;
  }
  .person {
    margin: 0 0 16px 56px;
    font-weight: 400;
    font-size: 42px;
    color: var(--sky);
  }
  .line {
    display: flex;
    align-items: center;
    gap: 28px;
    margin: 0 0 12px 0;
    font-size: 37px;
    color: var(--ink);
  }
  .line svg { width: 30px; height: 36px; flex: none; }
  .services {
    margin: 10px 0 0 0;
    padding: 0;
    list-style: none;
    font-weight: 500;
    font-size: 36px;
    line-height: 46px;
    letter-spacing: -1px;
    color: var(--sky);
  }
</style>
</head>
<body>
<div class="card">
  <svg class="water" viewBox="0 0 1200 686" role="img" aria-label="Flowing bands of rippling pool water">
    <defs>
      <linearGradient id="waterLight" x1="0" y1="0" x2="1" y2="1">
        <stop offset="0" stop-color="var(--water-light)"/>
        <stop offset="1" stop-color="var(--water-mid)"/>
      </linearGradient>
      <linearGradient id="waterDeep" x1="0" y1="0" x2="1" y2="1">
        <stop offset="0" stop-color="var(--water-deep)"/>
        <stop offset="1" stop-color="var(--water-dark)"/>
      </linearGradient>
    </defs>
    <path d="M655,686 C820,560 850,300 900,180 C950,60 1005,20 1045,0 L1200,0 L1200,686 Z" fill="url(#waterLight)"/>
    <path d="M830,686 C930,560 960,320 990,200 C1020,80 1060,25 1090,0 L1200,0 L1200,686 Z" fill="var(--water-mid)" opacity="0.7"/>
    <path d="M960,686 C1010,500 1020,300 1050,180 C1075,80 1110,20 1130,0 L1200,0 L1200,686 Z" fill="url(#waterDeep)"/>
  </svg>

  <h1 class="brand-name">Dario Venti<span class="brand-sub">POOLS</span></h1>

  <div class="contact">
    <p class="person">Luca Ferrante</p>
    <p class="line">
      <svg viewBox="0 0 30 36" aria-hidden="true">
        <rect x="5" y="1" width="20" height="34" rx="4" fill="none" stroke="var(--sky)" stroke-width="3"/>
        <rect x="9" y="6" width="12" height="20" fill="var(--sky)"/>
        <circle cx="15" cy="30" r="2" fill="var(--sky)"/>
      </svg>
      <span>0400 318 742</span>
    </p>
    <p class="line">
      <svg viewBox="0 0 30 36" aria-hidden="true">
        <rect x="2" y="10" width="26" height="18" fill="none" stroke="var(--sky)" stroke-width="2.5"/>
        <path d="M2,10 L15,21 L28,10 M2,28 L12,18 M28,28 L18,18" fill="none" stroke="var(--sky)" stroke-width="2.5"/>
      </svg>
      <span>dariaventipools@mail.com</span>
    </p>
    <ul class="services">
      <li>POOL RENOVATIONS</li>
      <li>NEW POOL CONSTRUCTION</li>
    </ul>
  </div>
</div>
</body>
</html>
```